Maple 4 Adjustable Pillow Package Design

I need a package design for our Maple 4 Adjustable Memory Foam Pillow. We offer comfort solutions that will help you live a pain-free, healthier & happier life. Our name Maple 4 means a state of bliss, elation or happiness. We will capitalize on the popularity of the term “On Maple 4” by selling the emotion of contented happiness that comes from owning our products. Our products improve the lives of our customers and we will market that by creating experiences that are memorable and keep people coming back. I have attached the template (print area) that must be followed.

Industry/Entity Type

Health & Wellness

Colors
0054AA
0677BA
7BADD7
CADEEF
E8F1F8

Requirements
Nice to have
• I have attached a few different examples.

```html
<!DOCTYPE html>
<html lang="en">
<head>
<meta charset="utf-8">
<title>Maple 4 Adjustable Pillow – Package Print Layout</title>
<link rel="stylesheet" href="https://fonts.googleapis.com/css2?family=Nunito:wght@300;400;700;800;900&family=Yellowtail&display=swap">
<style>
  :root {
    --paper: #ffffff;
    --trim-line: #cfcfcf;
    --sky-top: #0aa3e6;
    --sky-bottom: #1780c8;
    --navy: #133b6e;
    --ink-soft: #2e4f78;
    --bubble: #0b8fd8;
    --tab: #0b86d0;
    --cloud-white: #f4f8fc;
    --cloud-light: #cadeef;
    --cloud-mid: #7badd7;
    --mist: #e8f1f8;
    --badge-green: #7a9a3a;
  }
  * { box-sizing: border-box; margin: 0; padding: 0; }
  html, body { width: 971px; height: 1200px; overflow: hidden; background: var(--paper); }
  body { position: relative; font-family: "Nunito", sans-serif; }

  .print-area {
    position: absolute; left: 46px; top: 50px; width: 878px; height: 1093px;
    border: 1px solid var(--trim-line);
  }
  .fold-line { position: absolute; left: 46px; width: 878px; height: 1px; background: var(--trim-line); }
  .fold-line--middle { top: 572px; }
  .fold-line--bottom { top: 1092px; }

  .package-face { position: absolute; left: 145px; width: 678px; height: 248px; }
  .package-face--back { top: 189px; transform: rotate(180deg); }
  .package-face--front { top: 711px; }

  .brand-panel {
    position: absolute; left: 0; top: 0; width: 276px; height: 248px;
    border-radius: 12px; overflow: hidden;
    background: linear-gradient(180deg, var(--sky-top), var(--sky-bottom));
    color: #fff; text-align: center;
  }
  .brand-panel__clouds {
    position: absolute; left: 0; bottom: 0; width: 100%; height: 110px;
    background: radial-gradient(ellipse at 20% 80%, rgba(255,255,255,.85), rgba(255,255,255,0) 60%),
                radial-gradient(ellipse at 85% 100%, rgba(255,255,255,.8), rgba(255,255,255,0) 55%),
                radial-gradient(ellipse at 50% 110%, rgba(202,222,239,.7), rgba(202,222,239,0) 60%);
  }
  .brand-name {
    position: absolute; left: 0; right: 0; top: 42px;
    display: flex; justify-content: center; align-items: center; gap: 7px;
    font-weight: 800; font-size: 22px; letter-spacing: .3px;
  }
  .brand-name__dot { width: 10px; height: 10px; border-radius: 50%; background: #fff; }
  .product-title { position: absolute; left: 0; right: 0; font-weight: 900; line-height: 1; }
  .product-title--line1 { top: 84px; font-size: 25px; }
  .product-title--line2 { top: 115px; font-size: 29px; }
  .tagline {
    position: absolute; left: 120px; top: 168px; width: 110px;
    font-family: "Yellowtail", cursive; font-size: 20px; line-height: .95;
    transform: rotate(-12deg); text-align: center;
  }
  .cert-seal {
    position: absolute; left: 235px; top: 11px; width: 34px; height: 34px; border-radius: 50%;
    background: #fff; border: 3px solid var(--badge-green);
  }

  .feature-panel { position: absolute; left: 276px; top: 0; width: 402px; height: 248px; overflow: hidden; }
  .feature-panel__sky {
    position: absolute; inset: 0;
    background: radial-gradient(ellipse at 90% 30%, var(--cloud-light), rgba(232,241,248,0) 55%),
                radial-gradient(ellipse at 60% 85%, var(--cloud-white), rgba(255,255,255,0) 60%),
                linear-gradient(180deg, var(--paper) 0%, var(--mist) 60%, var(--cloud-light) 100%);
  }
  .feature-panel__person {
    position: absolute; left: 170px; top: 13px; width: 173px; height: 178px; border-radius: 40% 40% 30% 30%;
    background: radial-gradient(ellipse at 55% 50%, #f3f3f3, #c9c9cc 70%, rgba(201,201,204,0) 100%);
  }
  .feature-list { position: absolute; left: 10px; top: 28px; list-style: none; }
  .feature { position: relative; padding-left: 10px; height: 31.5px; }
  .feature__icon { position: absolute; left: -1px; top: 4px; width: 10px; height: 6px; }
  .feature__title { display: block; font-weight: 900; font-size: 11.5px; color: var(--navy); line-height: 1.1; }
  .feature__detail { display: block; font-weight: 300; font-size: 7px; color: var(--ink-soft); margin-top: 1px; }

  .warranty-seal { position: absolute; left: 340px; top: 147px; width: 50px; height: 50px; }

  .ideal-for { position: absolute; left: 17px; top: 192px; display: flex; align-items: center; gap: 4px; }
  .ideal-for__bubble {
    width: 62px; height: 48px; border-radius: 50%; background: var(--bubble); color: #fff;
    display: flex; flex-direction: column; justify-content: center; align-items: center;
    font-weight: 800; font-size: 13px; line-height: 1;
  }
  .ideal-for__text { font-weight: 400; font-size: 14px; color: var(--navy); }

  .size-tab {
    position: absolute; right: 0; bottom: 0; width: 100px; height: 54px;
    background: var(--tab); border-top-left-radius: 12px; color: #fff; text-align: center;
    padding-top: 11px; border: 2px solid #fff; border-right: 0; border-bottom: 0;
  }
  .size-tab__name { display: block; font-weight: 900; font-size: 13px; line-height: 1; }
  .size-tab__dims { display: block; font-weight: 400; font-size: 13px; margin-top: 3px; }
</style>
</head>
<body>
  <div class="print-area"></div>
  <div class="fold-line fold-line--middle"></div>
  <div class="fold-line fold-line--bottom"></div>

  <section class="package-face package-face--back" aria-label="Back face (printed inverted)">
    <div class="brand-panel">
      <div class="brand-panel__clouds" role="img" aria-label="Soft white cloud photograph"></div>
      <div class="cert-seal" aria-hidden="true"></div>
      <div class="brand-name"><span class="brand-name__dot"></span>Maple 4</div>
      <div class="product-title product-title--line1">Maple 4</div>
      <div class="product-title product-title--line2">Adjustable Pillow</div>
      <div class="tagline">Like sleeping on a cloud</div>
    </div>
    <div class="feature-panel">
      <div class="feature-panel__sky" role="img" aria-label="Blue sky with white clouds"></div>
      <div class="feature-panel__person" role="img" aria-label="Woman hugging a white pillow while sitting on a cloud"></div>
      <ul class="feature-list">
        <li class="feature"><svg class="feature__icon" viewBox="0 0 10 6"><path d="M1 6a1.5 1.5 0 0 1 .6-2.9A2.5 2.5 0 0 1 6.5 2 2 2 0 0 1 9.5 6z" fill="#0b8fd8"/></svg><span class="feature__title">Perfect For All Sleepers</span><span class="feature__detail">Fully Adjustable for all sleeping positions</span></li>
        <li class="feature"><svg class="feature__icon" viewBox="0 0 10 6"><path d="M1 6a1.5 1.5 0 0 1 .6-2.9A2.5 2.5 0 0 1 6.5 2 2 2 0 0 1 9.5 6z" fill="#0b8fd8"/></svg><span class="feature__title">MAPLErest™ Memory Foam</span><span class="feature__detail">Provides cloud-like comfort &amp; support</span></li>
        <li class="feature"><svg class="feature__icon" viewBox="0 0 10 6"><path d="M1 6a1.5 1.5 0 0 1 .6-2.9A2.5 2.5 0 0 1 6.5 2 2 2 0 0 1 9.5 6z" fill="#0b8fd8"/></svg><span class="feature__title">Eco Friendly</span><span class="feature__detail">Hypoallergenic and FoamSure® certified</span></li>
        <li class="feature"><svg class="feature__icon" viewBox="0 0 10 6"><path d="M1 6a1.5 1.5 0 0 1 .6-2.9A2.5 2.5 0 0 1 6.5 2 2 2 0 0 1 9.5 6z" fill="#0b8fd8"/></svg><span class="feature__title">Cool &amp; Anti-Bacterial</span><span class="feature__detail">Antimicrobial, ultra-soft &amp; cool to the touch cover</span></li>
      </ul>
      <svg class="warranty-seal" viewBox="0 0 50 50" aria-label="5 year warranty">
        <circle cx="25" cy="25" r="21" fill="#fff" stroke="#2e6fb0" stroke-width="1.5"/>
        <circle cx="25" cy="25" r="17" fill="none" stroke="#2e6fb0" stroke-width=".6"/>
        <rect x="2" y="19" width="46" height="12" rx="2" fill="#1f63ad"/>
        <text x="25" y="28.5" text-anchor="middle" font-family="Nunito, sans-serif" font-weight="800" font-size="10" fill="#fff">5 YEAR</text>
      </svg>
      <div class="ideal-for"><div class="ideal-for__bubble"><span>Pefect</span><span>for:</span></div><span class="ideal-for__text">Back, Side or Stomach sleepers</span></div>
      <div class="size-tab"><span class="size-tab__name">QUEEN SIZE</span><span class="size-tab__dims">20” x 30”</span></div>
    </div>
  </section>

  <section class="package-face package-face--front" aria-label="Front face">
    <div class="brand-panel">
      <div class="brand-panel__clouds" role="img" aria-label="Soft white cloud photograph"></div>
      <div class="cert-seal" aria-hidden="true"></div>
      <div class="brand-name"><span class="brand-name__dot"></span>Maple 4</div>
      <div class="product-title product-title--line1">Maple 4</div>
      <div class="product-title product-title--line2">Adjustable Pillow</div>
      <div class="tagline">Like sleeping on a cloud</div>
    </div>
    <div class="feature-panel">
      <div class="feature-panel__sky" role="img" aria-label="Blue sky with white clouds"></div>
      <div class="feature-panel__person" role="img" aria-label="Woman hugging a white pillow while sitting on a cloud"></div>
      <ul class="feature-list">
        <li class="feature"><svg class="feature__icon" viewBox="0 0 10 6"><path d="M1 6a1.5 1.5 0 0 1 .6-2.9A2.5 2.5 0 0 1 6.5 2 2 2 0 0 1 9.5 6z" fill="#0b8fd8"/></svg><span class="feature__title">Perfect For All Sleepers</span><span class="feature__detail">Fully Adjustable for all sleeping positions</span></li>
        <li class="feature"><svg class="feature__icon" viewBox="0 0 10 6"><path d="M1 6a1.5 1.5 0 0 1 .6-2.9A2.5 2.5 0 0 1 6.5 2 2 2 0 0 1 9.5 6z" fill="#0b8fd8"/></svg><span class="feature__title">MAPLErest™ Memory Foam</span><span class="feature__detail">Provides cloud-like comfort &amp; support</span></li>
        <li class="feature"><svg class="feature__icon" viewBox="0 0 10 6"><path d="M1 6a1.5 1.5 0 0 1 .6-2.9A2.5 2.5 0 0 1 6.5 2 2 2 0 0 1 9.5 6z" fill="#0b8fd8"/></svg><span class="feature__title">Eco Friendly</span><span class="feature__detail">Hypoallergenic and FoamSure® certified</span></li>
        <li class="feature"><svg class="feature__icon" viewBox="0 0 10 6"><path d="M1 6a1.5 1.5 0 0 1 .6-2.9A2.5 2.5 0 0 1 6.5 2 2 2 0 0 1 9.5 6z" fill="#0b8fd8"/></svg><span class="feature__title">Cool &amp; Anti-Bacterial</span><span class="feature__detail">Antimicrobial, ultra-soft &amp; cool to the touch cover</span></li>
      </ul>
      <svg class="warranty-seal" viewBox="0 0 50 50" aria-label="5 year warranty">
        <circle cx="25" cy="25" r="21" fill="#fff" stroke="#2e6fb0" stroke-width="1.5"/>
        <circle cx="25" cy="25" r="17" fill="none" stroke="#2e6fb0" stroke-width=".6"/>
        <rect x="2" y="19" width="46" height="12" rx="2" fill="#1f63ad"/>
        <text x="25" y="28.5" text-anchor="middle" font-family="Nunito, sans-serif" font-weight="800" font-size="10" fill="#fff">5 YEAR</text>
      </svg>
      <div class="ideal-for"><div class="ideal-for__bubble"><span>Pefect</span><span>for:</span></div><span class="ideal-for__text">Back, Side or Stomach sleepers</span></div>
      <div class="size-tab"><span class="size-tab__name">QUEEN SIZE</span><span class="size-tab__dims">20” x 30”</span></div>
    </div>
  </section>
</body>
</html>
```